Business Card Design Needed

Business car design required, logo will be supplied.

Brambleford Power Surveyors are looking to become the leading provider of energy performance certificates to estate agents, landlords and home owners in the Yorkshire region of the UK.

The business card must be double sided and professional looking. Estate agents receive hundreds of cards from contractors and our card must stand out.

I require a two sided business card that is clean, modern and created by a designer that can think outside of the box.

Brand colours can be supplied .

Please ask if you have any questions.

Target Market(s)

Estate agents, landlords and property owners

Industry/Entity Type

Property - estate agency - energy consultants

Contact Information for Business Card

Tomas Rendell - Energy Assessor - 07311642705 - www.BramblefordPSV.co.uk - info@bramblefordpsv.co.uk

Font styles to use
Serif
Sans Serif

Colors
00AB8E
00BBA5
67D7C9
C6EFE9
E9F9F6

Requirements
Must have
• Use the provided logo, clean, professional and stand out from the crowd
Nice to have
• Clever use of text, spacing and brand colours
Should not have
• Clip art

```html
<!DOCTYPE html>
<html lang="en">
<head>
<meta charset="utf-8">
<title>Brambleford Power Surveyors – Business Card</title>
<link href="https://fonts.googleapis.com/css2?family=Open+Sans:wght@400;700&display=swap" rel="stylesheet">
<style>
  :root {
    --brand-blue: #1b5e96;
    --brand-green: #a9c42c;
    --faint-blue: #e3ebf3;
    --text-grey: #4a4a4a;
    --card-white: #ffffff;
    --card-shade: #ececec;
    --backdrop: #2e2e2e;
  }
  * { margin: 0; padding: 0; box-sizing: border-box; }
  html, body {
    width: 1200px;
    height: 900px;
    overflow: hidden;
    background: var(--backdrop);
    font-family: "Open Sans", sans-serif;
  }
  .card {
    position: absolute;
    left: 230px;
    width: 740px;
    height: 420px;
    background: linear-gradient(135deg, var(--card-white) 0%, var(--card-shade) 100%);
    overflow: hidden;
  }
  .card--front { top: 25px; }
  .card--back { top: 455px; }

  .brand {
    position: absolute;
    display: flex;
    align-items: center;
  }
  .brand__dot {
    width: 58px;
    height: 58px;
    border-radius: 50%;
    border: 6px solid var(--brand-blue);
  }
  .brand__divider {
    width: 2px;
    height: 70px;
    background: var(--brand-blue);
    margin: 0 22px;
  }
  .brand__name {
    color: var(--brand-blue);
    font-weight: 400;
    font-size: 30px;
    line-height: 1.15;
    letter-spacing: 0.5px;
    text-transform: uppercase;
  }
  .card--front .brand { left: 110px; top: 170px; }
  .card--back .brand { left: 40px; top: 95px; }
  .card--back .brand__name { font-size: 26px; }

  .backdrop-circle {
    position: absolute;
    left: 420px;
    top: 10px;
    width: 300px;
    height: 300px;
    border-radius: 50%;
    border: 22px solid var(--faint-blue);
  }

  .holder {
    position: absolute;
    left: 40px;
    top: 300px;
    display: flex;
    align-items: baseline;
    gap: 8px;
  }
  .holder__name {
    color: var(--brand-blue);
    font-weight: 700;
    font-size: 22px;
    text-transform: uppercase;
  }
  .holder__sep,
  .contacts__sep {
    width: 1.5px;
    height: 20px;
    background: var(--brand-green);
    align-self: center;
  }
  .holder__role {
    color: var(--text-grey);
    font-size: 18px;
  }
  .rule {
    position: absolute;
    left: 40px;
    right: 40px;
    top: 338px;
    height: 2px;
    background: var(--brand-green);
  }
  .contacts {
    position: absolute;
    left: 40px;
    top: 352px;
    display: flex;
    align-items: center;
    gap: 10px;
    color: var(--text-grey);
    font-size: 15.5px;
  }
  .contact { display: flex; align-items: center; gap: 6px; }
  .contact__icon { width: 16px; height: 16px; fill: var(--brand-blue); }
</style>
</head>
<body>

  <section class="card card--front" aria-label="Card front">
    <div class="brand">
      <div class="brand__dot"></div>
      <div class="brand__divider"></div>
      <div class="brand__name">Brambleford<br>Power Surveyors</div>
    </div>
  </section>

  <section class="card card--back" aria-label="Card back">
    <div class="backdrop-circle"></div>
    <div class="brand">
      <div class="brand__dot"></div>
      <div class="brand__divider"></div>
      <div class="brand__name">Brambleford<br>Power Surveyors</div>
    </div>

    <div class="holder">
      <span class="holder__name">Tomas Rendell</span>
      <span class="holder__sep"></span>
      <span class="holder__role">Energy Assessor</span>
    </div>

    <div class="rule"></div>

    <div class="contacts">
      <span class="contact">
        <svg class="contact__icon" viewBox="0 0 24 24" aria-hidden="true"><path d="M6.6 10.8a15.1 15.1 0 0 0 6.6 6.6l2.2-2.2a1 1 0 0 1 1-.25 11.4 11.4 0 0 0 3.6.57 1 1 0 0 1 1 1V20a1 1 0 0 1-1 1A17 17 0 0 1 3 4a1 1 0 0 1 1-1h3.5a1 1 0 0 1 1 1c0 1.25.2 2.45.57 3.57a1 1 0 0 1-.25 1z"/></svg>
        07311642705
      </span>
      <span class="contacts__sep"></span>
      <span class="contact">
        <svg class="contact__icon" viewBox="0 0 24 24" aria-hidden="true"><path d="M3 5h18a1 1 0 0 1 1 1v12a1 1 0 0 1-1 1H3a1 1 0 0 1-1-1V6a1 1 0 0 1 1-1zm9 7.5L4.5 7.2v1.9L12 14.4l7.5-5.3V7.2z"/></svg>
        info@bramblefordpsv.co.uk
      </span>
      <span class="contacts__sep"></span>
      <span class="contact">
        <svg class="contact__icon" viewBox="0 0 24 24" aria-hidden="true"><path d="M12 2a10 10 0 1 0 0 20 10 10 0 0 0 0-20zm6.9 6h-2.9a15.7 15.7 0 0 0-1.4-3.6A8 8 0 0 1 18.9 8zM12 4c.8 1.2 1.5 2.5 1.9 4h-3.8c.4-1.5 1.1-2.8 1.9-4zM4.3 14a8.2 8.2 0 0 1 0-4h3.4a16.5 16.5 0 0 0 0 4zm.8 2h2.9c.3 1.3.8 2.5 1.4 3.6A8 8 0 0 1 5.1 16zM8 8H5.1a8 8 0 0 1 4.3-3.6C8.8 5.5 8.3 6.7 8 8zm4 12c-.8-1.2-1.5-2.5-1.9-4h3.8c-.4 1.5-1.1 2.8-1.9 4zm2.3-6H9.7a14.7 14.7 0 0 1 0-4h4.6a14.7 14.7 0 0 1 0 4zm.3 5.6c.6-1.1 1.1-2.3 1.4-3.6h2.9a8 8 0 0 1-4.3 3.6zm1.7-5.6a16.5 16.5 0 0 0 0-4h3.4a8.2 8.2 0 0 1 0 4z"/></svg>
        www.BramblefordPSV.co.uk
      </span>
    </div>
  </section>

</body>
</html>
```